Global investment holding company - Business Card Design

Kestrel Vane is a recently incorporated investment holding company. Based in Singapore, it has operations in global emerging markets in the transport & logistics, energy and livestock industries.

Its tagline "Alliances for Growth" reflects the company's philosophy of helping countries progress through partnerships which generate employment and share benefits with its society.

We are looking for a business card that reflects our global presence - incorporating the logo design into the business card design. It must have a sophisticated, modern & corporate feel.

Target Market(s)

Investors and high level governmental officials

Industry/Entity Type

Investment

Requirements
Must have
• - Use of shades of blue in logo

-Profile picture

- Name: Dorian Pike
- Title: Chairman
- Email: dorian@kestrelvane-example.com
- Mob: +65 9104 5821
- Tel: +65 6418 2093
- DID: + 65 6418 2094
- Address: 74 Marlow Road, #08-03, Singapore 048312

- website: www.kestrelvane-example.com

```html
<!DOCTYPE html>
<html lang="en">
<head>
<meta charset="utf-8">
<title>Kestrel Vane – Business Card</title>
<link href="https://fonts.googleapis.com/css2?family=Open+Sans:wght@400;600;700&display=swap" rel="stylesheet">
<style>
  :root {
    --navy: #1d4f8f;
    --blue: #1a7dc0;
    --blue-deep: #0f5fa3;
    --blue-light: #2e98d6;
    --ink: #5a6068;
    --paper: #f4f5f7;
    --paper-shade: #e4e7ec;
    --pale-circle: #dde6f0;
    --backdrop: #8d8d8d;
    --white: #ffffff;
  }
  * { margin: 0; padding: 0; box-sizing: border-box; }
  html, body { width: 1200px; height: 792px; overflow: hidden; }
  body {
    background: var(--backdrop);
    font-family: "Open Sans", Arial, sans-serif;
    display: flex;
    align-items: center;
    justify-content: center;
    gap: 40px;
  }
  .card {
    position: relative;
    width: 540px;
    height: 310px;
    overflow: hidden;
    box-shadow: 0 10px 24px rgba(0,0,0,0.3);
  }

  /* Front */
  .card--front {
    background: linear-gradient(160deg, var(--white) 0%, var(--paper) 55%, var(--paper-shade) 100%);
  }
  .front__circle {
    position: absolute;
    width: 380px; height: 380px;
    border-radius: 50%;
    background: radial-gradient(circle at 40% 40%, #eef3f8 0%, var(--pale-circle) 100%);
    right: -70px; top: -60px;
  }
  .front__band {
    position: absolute; left: 0; right: 0; bottom: 0;
    height: 14px;
    background: linear-gradient(90deg, var(--blue-deep), var(--blue-light));
  }
  .brand {
    position: absolute; left: 30px; top: 62px;
    display: flex; align-items: center; gap: 14px;
  }
  .brand__dot {
    width: 56px; height: 56px; border-radius: 50%;
    background: var(--blue);
  }
  .brand__name {
    font-weight: 700; font-size: 28px; line-height: 1;
    color: var(--navy); text-transform: uppercase;
  }
  .brand__tagline {
    position: absolute; left: 52px; top: 132px;
    font-size: 11px; letter-spacing: 1.6px; color: var(--ink);
    text-transform: uppercase;
  }
  .contact {
    position: absolute; left: 48px; top: 196px;
    font-size: 11px; line-height: 15px; color: var(--ink);
    text-transform: uppercase; list-style: none;
  }
  .contact li { display: flex; align-items: center; gap: 6px; }
  .contact svg { width: 11px; height: 11px; flex: none; }
  .contact svg .fill { fill: var(--navy); }
  .contact svg .line { fill: none; stroke: var(--white); stroke-width: 1; }
  .portrait {
    position: absolute; right: 40px; top: 16px;
    width: 136px; height: 140px;
    border: 3px solid var(--blue);
    background: linear-gradient(170deg, #c9b79a 0%, #8a7a66 55%, #2a3446 100%);
  }
  .person {
    position: absolute; right: 40px; top: 168px; text-align: right;
  }
  .person__name { font-weight: 700; font-size: 19px; color: var(--navy); }
  .person__title { font-size: 9px; color: var(--ink); text-transform: uppercase; letter-spacing: 0.5px; }

  /* Back */
  .card--back {
    background: linear-gradient(135deg, var(--blue-deep) 0%, var(--blue) 55%, var(--blue-light) 100%);
    color: var(--white);
  }
  .back__circle {
    position: absolute;
    width: 300px; height: 300px; border-radius: 50%;
    background: rgba(255,255,255,0.08);
    left: 210px; top: 40px;
  }
  .back__brand {
    position: absolute; left: 120px; top: 70px;
    display: flex; align-items: center; gap: 18px;
  }
  .back__dot { width: 76px; height: 76px; border-radius: 50%; background: var(--white); }
  .back__name { font-weight: 700; font-size: 40px; line-height: 1; text-transform: uppercase; }
  .back__tagline {
    position: absolute; left: 120px; top: 168px;
    font-size: 14px; letter-spacing: 2px; text-transform: uppercase;
  }
  .back__web {
    position: absolute; left: 120px; top: 232px;
    font-size: 14px; letter-spacing: 1.5px;
  }
  .back__web strong { font-weight: 700; }
</style>
</head>
<body>
  <section class="card card--front">
    <div class="front__circle"></div>
    <div class="brand">
      <div class="brand__dot"></div>
      <div class="brand__name">Kestrel<br>Vane</div>
    </div>
    <p class="brand__tagline">Alliances for Growth</p>
    <ul class="contact">
      <li>74 Marlow Road, #08-03</li>
      <li>Singapore 048312</li>
      <li><svg viewBox="0 0 12 12"><rect class="fill" x="0.5" y="2.5" width="11" height="7" rx="0.8"/><path class="line" d="M1 3l5 4 5-4"/></svg>dorian@kestrelvane-example.com</li>
      <li><svg viewBox="0 0 12 12"><rect class="fill" x="3" y="0.5" width="6" height="11" rx="1"/></svg>+65 9104 5821</li>
      <li><svg viewBox="0 0 12 12"><rect class="fill" x="1" y="4" width="10" height="7" rx="1"/><rect class="fill" x="2" y="1" width="8" height="3" rx="1"/></svg>+65 6418 2093</li>
      <li><svg viewBox="0 0 12 12"><rect class="fill" x="1" y="5" width="10" height="6" rx="1"/><rect class="fill" x="3" y="1" width="6" height="4"/></svg>+ 65 6418 2094</li>
    </ul>
    <div class="portrait" role="img" aria-label="Portrait photograph of the chairman"></div>
    <div class="person">
      <p class="person__name">Dorian Pike</p>
      <p class="person__title">Chairman</p>
    </div>
    <div class="front__band"></div>
  </section>

  <section class="card card--back">
    <div class="back__circle"></div>
    <div class="back__brand">
      <div class="back__dot"></div>
      <div class="back__name">Kestrel<br>Vane</div>
    </div>
    <p class="back__tagline">Alliances for Growth</p>
    <p class="back__web">www.<strong>kestrelvane-example</strong>.com</p>
  </section>
</body>
</html>
```